Brackwater Construction

We need to do a design with our logo on our cars. Both of the directors have Mirvano dorvak utes.

Reason: I still want to see more designs

Target Market(s)

just advertising

Industry/Entity Type

Building

Font styles to use
Sans Serif
Script

Colors
0255a3
3176b5
85acd3
cfdeed
ffffff

Requirements
Must have
• signage on the side of the car and the back tailgate.
Nice to have
• our website(currently being upgraded) numbers aren't super important but id like our name and the words " A professional approach to quality construction" (See website)

```html
<!DOCTYPE html>
<html lang="en">
<head>
<meta charset="utf-8">
<title>Brackwater Construction – Vehicle Signage</title>
<link href="https://fonts.googleapis.com/css2?family=Tinos:wght@400;700&family=Roboto+Condensed:wght@400&display=swap" rel="stylesheet">
<style>
  :root{
    --ink:#111111;
    --brand-blue:#1e3ee6;
    --panel:#ffffff;
    --page:#f2f2f2;
    --edge:#d4d4d4;
  }
  html,body{margin:0;padding:0;overflow:hidden;}
  body{width:1200px;height:1200px;background:var(--page);position:relative;font-family:'Tinos',serif;color:var(--ink);}
  .sign{position:absolute;background:var(--panel);border:1px solid var(--edge);}
  .tagline{font-family:'Tinos',serif;font-weight:700;text-align:center;line-height:1.35;}
  .name{font-family:'Tinos',serif;font-weight:700;white-space:nowrap;}
  .web{font-family:'Roboto Condensed',sans-serif;color:var(--brand-blue);white-space:nowrap;}
  .phones{font-family:'Roboto Condensed',sans-serif;white-space:nowrap;letter-spacing:1px;}
  .phones .sep{color:var(--brand-blue);padding:0 8px;}
  .mark{position:absolute;display:flex;flex-direction:column;align-items:center;gap:10px;}
  .mark-square{background:var(--brand-blue);}
  .mark-name{font-family:'Tinos',serif;font-weight:700;color:var(--ink);white-space:nowrap;}
  .abs{position:absolute;}
</style>
</head>
<body>

  <!-- Passenger side: tub panel -->
  <div class="sign" style="left:60px;top:70px;width:330px;height:110px;">
    <div class="tagline abs" style="left:0;right:0;top:28px;font-size:20px;">A Professional Approach<br>To Quality Construction And Design</div>
  </div>
  <!-- Passenger side: door panel -->
  <div class="sign" style="left:420px;top:70px;width:720px;height:250px;">
    <div class="abs" style="left:34px;top:50px;">
      <div class="name" style="font-size:34px;">Brackwater Construction</div>
      <div class="web" style="font-size:26px;margin-top:10px;">www.brackwaterconstruction.com.au</div>
      <div class="phones" style="font-size:30px;margin-top:12px;">0400 555 017<span class="sep">|</span>0428 555 092</div>
    </div>
    <div class="mark" style="right:40px;top:40px;">
      <div class="mark-square" style="width:110px;height:110px;"></div>
      <div class="mark-name" style="font-size:24px;">Brackwater</div>
    </div>
  </div>

  <!-- Driver side: door panel -->
  <div class="sign" style="left:60px;top:380px;width:720px;height:250px;">
    <div class="mark" style="left:40px;top:40px;">
      <div class="mark-square" style="width:110px;height:110px;"></div>
      <div class="mark-name" style="font-size:24px;">Brackwater</div>
    </div>
    <div class="abs" style="left:220px;top:50px;">
      <div class="name" style="font-size:34px;">Brackwater Construction</div>
      <div class="web" style="font-size:26px;margin-top:10px;">www.brackwaterconstruction.com.au</div>
      <div class="phones" style="font-size:30px;margin-top:12px;">0400 555 017<span class="sep">|</span>0428 555 092</div>
    </div>
  </div>
  <!-- Driver side: tub panel -->
  <div class="sign" style="left:810px;top:380px;width:330px;height:110px;">
    <div class="tagline abs" style="left:0;right:0;top:28px;font-size:20px;">A Professional Approach<br>To Quality Construction And Design</div>
  </div>

  <!-- Tailgate panel -->
  <div class="sign" style="left:160px;top:700px;width:880px;height:340px;">
    <div class="mark" style="left:40px;top:40px;">
      <div class="mark-square" style="width:150px;height:150px;"></div>
      <div class="name" style="font-size:30px;text-align:center;line-height:1.15;margin-top:8px;">Brackwater<br>Construction</div>
    </div>
    <div class="tagline abs" style="left:260px;right:40px;top:90px;font-size:36px;">A Professional Approach To<br>Quality Construction And Design</div>
    <div class="web abs" style="left:260px;right:40px;top:232px;font-size:30px;color:var(--ink);text-align:center;">www.brackwaterconstruction.com.au</div>
  </div>

</body>
</html>
```